Bramblecove Suite Complementary Pass

I’d like a complimentary pass for any 30-minute Bramblecove Suite session. Choose one of the following options: Infrared Sauna with Red Light, Massage Chair Velquora Compression Therapy, or Paraffin Wax Hand Bath.

Please incorporate the logo and brand colors into your design. I’d like a square image that will be printed on square business cards (no rectangles).

Please refer to the logo and menu for more details.

Contact Information for Business Card

See discretion

```html
<!DOCTYPE html>
<html lang="en">
<head>
<meta charset="utf-8">
<title>Marisol Physical Therapy – Complimentary Recovery Pass</title>
<link rel="stylesheet" href="https://fonts.googleapis.com/css2?family=Playfair+Display:wght@400;500&family=Playball&family=Roboto:ital,wght@0,400;0,500;1,400&display=swap">
<style>
  :root {
    --stage: #bfbfbf;
    --card: #fff8f8;
    --violet: #5a429a;
    --coral: #f1684a;
    --white: #ffffff;
  }
  * { margin: 0; padding: 0; box-sizing: border-box; }
  html, body {
    width: 1200px; height: 1137px; overflow: hidden;
    background: var(--stage);
    font-family: "Roboto", Arial, sans-serif;
    color: var(--white);
  }
  .pass {
    position: absolute; left: 192px; top: 158px;
    width: 829px; height: 830px;
    background: var(--card);
  }
  .pass-face {
    position: absolute; left: 27px; top: 27px;
    width: 776px; height: 776px;
    background: var(--violet);
    border: 2px solid var(--coral);
    overflow: hidden;
  }
  .brand {
    position: absolute; top: 78px; left: 0; width: 100%;
    display: flex; align-items: center; justify-content: center; gap: 14px;
  }
  .brand-mark { width: 26px; height: 26px; background: var(--coral); }
  .brand-name { font-size: 30px; font-weight: 500; letter-spacing: 0.5px; }
  .headline {
    position: absolute; top: 180px; left: 0; width: 100%;
    text-align: center;
    font-family: "Playfair Display", Georgia, serif;
    font-weight: 400;
    font-size: 56px; line-height: 1;
  }
  .headline .script {
    font-family: "Playball", cursive;
    font-weight: 400;
    font-size: 68px;
  }
  .subhead {
    position: absolute; top: 248px; left: 0; width: 100%;
    text-align: center;
    font-family: "Playfair Display", Georgia, serif;
    font-weight: 500; font-size: 45px; color: var(--coral);
  }
  .prompt {
    position: absolute; top: 342px; left: 0; width: 100%;
    text-align: center; font-style: italic; font-size: 24px;
  }
  .options {
    position: absolute; top: 392px; left: 0; right: 0; height: 268px;
    background: var(--coral);
    list-style: none; padding-top: 26px;
  }
  .option {
    position: relative; height: 53px;
    font-size: 26px; line-height: 53px;
  }
  .option-box {
    position: absolute; left: 56px; top: 18px;
    width: 17px; height: 17px; border: 2px solid var(--white);
  }
  .option-name { position: absolute; left: 101px; }
  .option-saving { position: absolute; left: 568px; }
  .redeem {
    position: absolute; top: 685px; left: 0; width: 100%;
    text-align: center; font-style: italic; font-size: 25px;
  }
  .expiry {
    position: absolute; top: 729px; left: 0; width: 100%;
    text-align: center; font-size: 18px;
  }
</style>
</head>
<body>
  <main class="pass">
    <section class="pass-face">
      <div class="brand">
        <span class="brand-mark"></span>
        <span class="brand-name">Marisol Physical Therapy</span>
      </div>

      <h1 class="headline">Enjoy a <span class="script">Complimentary</span></h1>
      <h2 class="subhead">30-Minute Recovery Session</h2>

      <p class="prompt">Choose one of the following:</p>

      <ul class="options">
        <li class="option"><span class="option-box"></span><span class="option-name">Infrared Sauna + Red Light</span><span class="option-saving">( Save $40 )</span></li>
        <li class="option"><span class="option-box"></span><span class="option-name">Massage Chair</span><span class="option-saving">( Save $40 )</span></li>
        <li class="option"><span class="option-box"></span><span class="option-name">Velquora Compression Therapy</span><span class="option-saving">( Save $40 )</span></li>
        <li class="option"><span class="option-box"></span><span class="option-name">Paraffin Wax Hand Bath</span><span class="option-saving">( Save $50 )</span></li>
      </ul>

      <p class="redeem">Redeem at front desk or book your session today</p>
      <p class="expiry">Expiry DDMMYYYY</p>
    </section>
  </main>
</body>
</html>
```